Business card design needed

We need a business card design and possible logo for my new building construction business. I would like a masculine type of business design.

Thanks
Also can we please put my ABN number 47380926514 in as well thanks.
And use the colours black, orange and white. Cheers

Industry/Entity Type

Building

Contact Information for Business Card

Tarrow constructions, owner: Derek hollis, mobile:0417282613, email: hollo.d@quenmail.com, licence: 618374K

```html
<!DOCTYPE html>
<html lang="en">
<head>
<meta charset="utf-8">
<title>Tarrow Constructions – Business Card Options</title>
<link rel="stylesheet" href="https://fonts.googleapis.com/css2?family=Exo+2:wght@400;500;600;700&display=swap">
<style>
  :root {
    --canvas: #eceded;
    --paper: #ffffff;
    --ink: #1c1c1c;
    --ink-soft: #454545;
    --black: #111111;
    --charcoal: #2a2a2a;
    --orange: #f07a1a;
    --orange-light: #ffb066;
    --steel: #a9aaac;
    --label: #333333;
  }
  * { box-sizing: border-box; margin: 0; padding: 0; }
  html, body { width: 1200px; height: 795px; overflow: hidden; }
  body {
    background: var(--canvas);
    font-family: "Exo 2", sans-serif;
    color: var(--ink);
    position: relative;
  }
  .option-number {
    position: absolute;
    font-family: Arial, sans-serif;
    font-size: 22px;
    color: var(--label);
  }
  .card {
    position: absolute;
    width: 464px;
    height: 257px;
    background: var(--paper);
    overflow: hidden;
    box-shadow: 0 6px 10px rgba(0,0,0,0.18);
  }
  .card > * { position: absolute; }
  .name { font-size: 19px; font-weight: 600; white-space: nowrap; }
  .role, .licence, .abn { font-size: 12px; white-space: nowrap; }
  .contact { font-size: 15px; white-space: nowrap; display: flex; align-items: center; gap: 7px; }
  .contact svg { width: 12px; height: 12px; flex: none; }
  .wordmark { font-weight: 700; line-height: 1.05; white-space: nowrap; }

  /* Option 1 */
  .card-one { left: 88px; top: 89px; }
  .card-one .name { left: 41px; top: 58px; color: var(--ink); }
  .card-one .role { left: 41px; top: 84px; font-size: 11px; color: var(--ink-soft); }
  .card-one .licence { left: 41px; top: 100px; font-size: 11px; color: var(--ink-soft); }
  .card-one .abn { left: 41px; top: 116px; font-size: 11px; color: var(--ink-soft); }
  .card-one .contact { left: 40px; color: var(--ink-soft); }
  .card-one .phone { top: 140px; }
  .card-one .email { top: 161px; }
  .card-one .brand { left: 225px; top: 86px; display: flex; align-items: center; gap: 8px; }
  .card-one .brand-square { width: 40px; height: 40px; background: var(--orange); }
  .card-one .wordmark { color: var(--black); font-size: 20px; }
  .card-one .footer-band { left: 0; top: 214px; width: 464px; height: 43px; }
  .card-one .website { left: 30px; top: 224px; font-size: 13px; font-weight: 600; color: #fff; }

  /* Option 2 */
  .card-two { left: 90px; top: 435px; }
  .card-two .lower-panel {
    left: 0; top: 139px; width: 464px; height: 118px;
    background: linear-gradient(180deg, var(--charcoal) 0%, var(--black) 55%, #000 100%);
  }
  .card-two .accent-line { left: 0; top: 139px; width: 464px; height: 3px; background: var(--orange); }
  .card-two .brand { left: 95px; top: 36px; display: flex; align-items: center; gap: 10px; }
  .card-two .brand-square { width: 50px; height: 50px; background: var(--orange); }
  .card-two .wordmark { color: var(--black); font-size: 24px; }
  .card-two .divider { left: 218px; top: 148px; width: 2px; height: 103px; background: linear-gradient(180deg, rgba(240,122,26,0.1), rgba(240,122,26,0.9), rgba(240,122,26,0.1)); }
  .card-two .identity { right: 256px; top: 160px; text-align: right; color: #fff; }
  .card-two .identity .name { position: static; font-size: 19px; }
  .card-two .identity .role { margin-top: 1px; font-size: 11px; color: var(--orange-light); }
  .card-two .identity .licence { margin-top: 6px; font-size: 11px; }
  .card-two .identity .abn { margin-top: 2px; font-size: 11px; }
  .card-two .contacts { left: 232px; top: 178px; color: #fff; display: flex; flex-direction: column; gap: 5px; }
  .card-two .contact { font-size: 13px; font-weight: 500; }
  .card-two .contact svg { color: var(--orange); }

  /* Option 3 */
  .card-three {
    left: 655px; top: 87px;
    background: linear-gradient(90deg, #000 0%, #3a1d05 6%, var(--orange) 16%, var(--orange-light) 26%, #ffffff 40%, #e4e4e5 60%, var(--steel) 100%);
  }
  .card-three .brand { left: 146px; top: 48px; width: 96px; text-align: center; display: flex; justify-content: center; }
  .card-three .wordmark { color: var(--black); font-size: 16px; }
  .card-three .divider { left: 191px; top: 108px; width: 2px; height: 136px; background: linear-gradient(180deg, rgba(240,122,26,0), var(--orange) 30%, var(--orange) 70%, rgba(240,122,26,0)); }
  .card-three .identity { right: 282px; top: 130px; text-align: right; color: var(--ink); }
  .card-three .identity .name { position: static; font-size: 17px; font-weight: 500; }
  .card-three .identity .role { margin-top: 2px; font-size: 11px; }
  .card-three .identity .licence { margin-top: 6px; font-size: 11px; }
  .card-three .identity .abn { margin-top: 2px; font-size: 11px; }
  .card-three .contacts { left: 205px; top: 135px; display: flex; flex-direction: column; gap: 4px; color: var(--ink); }
  .card-three .contact { font-size: 14px; font-weight: 600; }

  /* Option 4 */
  .card-four { left: 653px; top: 440px; }
  .card-four .side-panel { left: 0; top: 0; width: 176px; height: 257px; background: var(--black); }
  .card-four .side-rule { left: 182px; top: 0; width: 4px; height: 257px; background: var(--orange); }
  .card-four .brand { left: 0; top: 165px; width: 176px; text-align: center; }
  .card-four .wordmark { color: #fff; font-size: 15px; line-height: 1.3; }
  .card-four .name { left: 208px; top: 62px; color: var(--black); font-size: 19px; }
  .card-four .role { left: 208px; top: 90px; font-size: 11px; color: var(--orange); }
  .card-four .licence { left: 208px; top: 106px; font-size: 11px; color: var(--ink-soft); }
  .card-four .abn { left: 208px; top: 121px; font-size: 11px; color: var(--ink-soft); }
  .card-four .contact { left: 208px; color: var(--ink-soft); font-size: 16px; }
  .card-four .phone { top: 149px; }
  .card-four .email { top: 170px; }
</style>
</head>
<body>
  <span class="option-number" style="left:60px;top:86px">1</span>
  <span class="option-number" style="left:629px;top:85px">3</span>
  <span class="option-number" style="left:63px;top:432px">2</span>
  <span class="option-number" style="left:627px;top:436px">4</span>

  <!-- Option 1 -->
  <section class="card card-one">
    <p class="name">Derek Hollis</p>
    <p class="role">Owner</p>
    <p class="licence">licence: 618374K</p>
    <p class="abn">ABN: 47380926514</p>
    <p class="contact phone">
      <svg viewBox="0 0 12 12"><rect x="2.5" y="0.5" width="7" height="11" rx="1" fill="none" stroke="currentColor"/><line x1="4.5" y1="9.5" x2="7.5" y2="9.5" stroke="currentColor"/></svg>
      0417282613</p>
    <p class="contact email">
      <svg viewBox="0 0 12 12"><rect x="0.5" y="2.5" width="11" height="7" fill="none" stroke="currentColor"/><polyline points="0.5,2.5 6,7 11.5,2.5" fill="none" stroke="currentColor"/></svg>
      hollo.d@quenmail.com</p>
    <div class="brand">
      <span class="brand-square"></span>
      <p class="wordmark">TARROW<br>CONSTRUCTIONS</p>
    </div>
    <svg class="footer-band" viewBox="0 0 464 43" preserveAspectRatio="none">
      <defs>
        <linearGradient id="band-dark" x1="0" y1="0" x2="0" y2="1">
          <stop offset="0" stop-color="#2a2a2a"/><stop offset="1" stop-color="#000"/>
        </linearGradient>
        <linearGradient id="band-light" x1="0" y1="0" x2="1" y2="0">
          <stop offset="0" stop-color="#c9560a"/><stop offset="1" stop-color="#ffb066"/>
        </linearGradient>
      </defs>
      <polygon points="0,0 220,0 250,22 464,22 464,43 0,43" fill="url(#band-dark)"/>
      <polygon points="222,2 464,2 464,16 244,16" fill="url(#band-light)"/>
    </svg>
    <p class="website">www.TarrowConstructions.com</p>
  </section>

  <!-- Option 3 -->
  <section class="card card-three">
    <div class="brand"><p class="wordmark">TARROW<br>CONSTRUCTIONS</p></div>
    <div class="divider"></div>
    <div class="identity">
      <p class="name">Derek Hollis</p>
      <p class="role">Owner</p>
      <p class="licence">licence: 618374K</p>
      <p class="abn">ABN: 47380926514</p>
    </div>
    <div class="contacts">
      <p class="contact"><svg viewBox="0 0 12 12"><rect x="2.5" y="0.5" width="7" height="11" rx="1" fill="none" stroke="currentColor"/><line x1="4.5" y1="9.5" x2="7.5" y2="9.5" stroke="currentColor"/></svg>0417282613</p>
      <p class="contact"><svg viewBox="0 0 12 12"><rect x="0.5" y="2.5" width="11" height="7" fill="none" stroke="currentColor"/><polyline points="0.5,2.5 6,7 11.5,2.5" fill="none" stroke="currentColor"/></svg>hollo.d@quenmail.com</p>
      <p class="contact"><svg viewBox="0 0 12 12"><circle cx="6" cy="6" r="5.3" fill="none" stroke="currentColor"/><ellipse cx="6" cy="6" rx="2.4" ry="5.3" fill="none" stroke="currentColor"/><line x1="0.7" y1="6" x2="11.3" y2="6" stroke="currentColor"/></svg>www.TarrowConstructions.com</p>
    </div>
  </section>

  <!-- Option 2 -->
  <section class="card card-two">
    <div class="lower-panel"></div>
    <div class="accent-line"></div>
    <div class="brand">
      <span class="brand-square"></span>
      <p class="wordmark">TARROW<br>CONSTRUCTIONS</p>
    </div>
    <div class="divider"></div>
    <div class="identity">
      <p class="name">Derek Hollis</p>
      <p class="role">Owner</p>
      <p class="licence">licence: 618374K</p>
      <p class="abn">ABN: 47380926514</p>
    </div>
    <div class="contacts">
      <p class="contact"><svg viewBox="0 0 12 12"><rect x="2.5" y="0.5" width="7" height="11" rx="1" fill="none" stroke="currentColor"/><line x1="4.5" y1="9.5" x2="7.5" y2="9.5" stroke="currentColor"/></svg>0417282613</p>
      <p class="contact"><svg viewBox="0 0 12 12"><rect x="0.5" y="2.5" width="11" height="7" fill="currentColor"/><polyline points="0.5,2.5 6,7 11.5,2.5" fill="none" stroke="#111111"/></svg>hollo.d@quenmail.com</p>
      <p class="contact"><svg viewBox="0 0 12 12"><circle cx="6" cy="6" r="5.3" fill="none" stroke="currentColor"/><ellipse cx="6" cy="6" rx="2.4" ry="5.3" fill="none" stroke="currentColor"/><line x1="0.7" y1="6" x2="11.3" y2="6" stroke="currentColor"/></svg>www.TarrowConstructions.com</p>
    </div>
  </section>

  <!-- Option 4 -->
  <section class="card card-four">
    <div class="side-panel"></div>
    <div class="side-rule"></div>
    <div class="brand"><p class="wordmark">TARROW<br>CONSTRUCTIONS</p></div>
    <p class="name">Derek Hollis</p>
    <p class="role">Owner</p>
    <p class="licence">licence: 618374K</p>
    <p class="abn">ABN: 47380926514</p>
    <p class="contact phone"><svg viewBox="0 0 12 12"><rect x="2.5" y="0.5" width="7" height="11" rx="1" fill="none" stroke="currentColor"/><line x1="4.5" y1="9.5" x2="7.5" y2="9.5" stroke="currentColor"/></svg>0417282613</p>
    <p class="contact email"><svg viewBox="0 0 12 12"><rect x="0.5" y="2.5" width="11" height="7" fill="none" stroke="currentColor"/><polyline points="0.5,2.5 6,7 11.5,2.5" fill="none" stroke="currentColor"/></svg>hollo.d@quenmail.com</p>
  </section>
</body>
</html>
```